Greta Polanski Consulting

I am starting my own business and want to have a business card that stands out from the rest. Class is the word i use to describe what i would like to my card to look like.

I see my card as vibrant red card with rounded edges. mat finish
Centered scripted writing
large scripted font: Greta Polanski, smaller font & not scripted: Consulting, next line 0438157226, next line greta@polanskihome.com.au

i have now left 2 email message for the design of my card. Family is spelt wrong on the card. this needs to be correct and finial proof sent though!!! before i can download and approve
Greta

Target Market(s)

Real Estate Professionals

Industry/Entity Type

Business

Contact Information for Business Card

Greta Polanski
Consulting
0438 157 226
greta@polanskihome.com.au

Logo Text

no logo

Requirements
Must have
• must have rounded edges

```html
<!DOCTYPE html>
<html lang="en">
<head>
<meta charset="utf-8">
<title>Greta Polanski Consulting – Business Card</title>
<link rel="stylesheet" href="https://fonts.googleapis.com/css2?family=Dancing+Script:wght@600&family=Jost:wght@300;400&display=swap">
<style>
  :root {
    --backdrop: #141414;
    --card-red: #cc3340;
    --card-red-light: #d8434f;
    --card-red-dark: #b32a36;
    --ink-white: #ffffff;
    --emboss-shadow: rgba(90, 10, 18, 0.55);
  }

  html, body {
    margin: 0;
    padding: 0;
    width: 1200px;
    height: 700px;
    overflow: hidden;
    background: var(--backdrop);
  }

  .canvas {
    width: 1200px;
    height: 700px;
    display: flex;
    align-items: center;
    justify-content: center;
  }

  .business-card {
    position: relative;
    width: 880px;
    height: 530px;
    border-radius: 44px;
    background:
      radial-gradient(ellipse at 35% 30%, var(--card-red-light) 0%, var(--card-red) 55%, var(--card-red-dark) 100%);
    display: flex;
    flex-direction: column;
    align-items: center;
    color: var(--ink-white);
    text-align: center;
    box-sizing: border-box;
    padding-top: 120px;
  }

  .card-name {
    margin: 0;
    font-family: "Dancing Script", cursive;
    font-weight: 600;
    font-size: 92px;
    line-height: 1;
    letter-spacing: 1px;
    text-shadow: 1px 2px 1px var(--emboss-shadow);
  }

  .card-tagline {
    margin: 22px 0 0;
    font-family: "Jost", sans-serif;
    font-weight: 300;
    font-size: 30px;
    letter-spacing: 12px;
    padding-left: 12px;
    text-transform: uppercase;
    text-shadow: 1px 1px 1px var(--emboss-shadow);
  }

  .card-contact {
    margin-top: 78px;
    font-family: "Jost", sans-serif;
    font-weight: 400;
    font-style: normal;
    line-height: 1.5;
    text-shadow: 1px 1px 1px var(--emboss-shadow);
  }

  .card-phone {
    display: block;
    font-size: 27px;
    letter-spacing: 1.5px;
  }

  .card-email {
    display: block;
    font-size: 24px;
    letter-spacing: 0.5px;
  }
</style>
</head>
<body>
  <main class="canvas">
    <section class="business-card" aria-label="Greta Polanski Consulting business card">
      <h1 class="card-name">Greta Polanski</h1>
      <p class="card-tagline">Consulting</p>
      <address class="card-contact">
        <span class="card-phone">0438 157 226</span>
        <span class="card-email">greta@polanskihome.com.au</span>
      </address>
    </section>
  </main>
</body>
</html>
```